Veltrano - Mechanic/Collision Center Business Card

We're looking for a business card design for our mechanic/ collision repair shop.

Can be with colours or monochromatic.

See the attached files.

Many thanks

```html
<!DOCTYPE html>
<html lang="pt">
<head>
<meta charset="utf-8">
<title>Veltrano – Business Card</title>
<link rel="stylesheet" href="https://fonts.googleapis.com/css2?family=Lato:wght@400;700;900&display=swap">
<style>
  :root {
    --backdrop: #5d5e60;
    --card: #1c1f23;
    --card-edge: #1d86c4;
    --accent: #2a9ee0;
    --text-light: #d9dce0;
    --text-muted: #aeb3b9;
  }
  * { box-sizing: border-box; margin: 0; padding: 0; }
  html, body {
    width: 1200px; height: 900px; overflow: hidden;
    background: var(--backdrop);
    font-family: "Lato", Arial, sans-serif;
  }
  .canvas {
    position: relative; width: 1200px; height: 900px;
    display: flex; flex-direction: column; align-items: center; justify-content: center; gap: 60px;
  }
  .card {
    position: relative; width: 600px; height: 345px;
    background: var(--card);
    border-bottom: 3px solid var(--card-edge);
    border-radius: 3px;
    box-shadow: 0 14px 30px rgba(0,0,0,.35);
    overflow: hidden;
  }
  .brand {
    display: flex; align-items: center; gap: 14px;
    color: var(--text-light); font-weight: 900; letter-spacing: 1px;
  }
  .brand-dot { border-radius: 50%; background: var(--accent); flex: none; }
  .brand-est {
    display: block; margin-top: 6px; text-align: center;
    font-size: 12px; font-weight: 700; letter-spacing: 2px; color: var(--text-muted);
  }
  /* front */
  .card-front { display: flex; align-items: center; justify-content: center; }
  .card-front .brand { font-size: 56px; }
  .card-front .brand-dot { width: 44px; height: 44px; }
  /* back */
  .card-back { display: flex; }
  .back-logo {
    width: 50%; padding-top: 80px;
    display: flex; flex-direction: column; align-items: center;
  }
  .back-logo .brand { font-size: 34px; gap: 10px; }
  .back-logo .brand-dot { width: 26px; height: 26px; }
  .divider {
    position: absolute; left: 50%; top: 130px; width: 1px; height: 160px;
    background: var(--card-edge);
  }
  .contact { width: 50%; padding: 120px 24px 0 26px; color: var(--text-light); }
  .contact-name { font-size: 25px; font-weight: 700; color: var(--accent); line-height: 1; }
  .contact-role { font-size: 13px; color: var(--text-muted); margin: 4px 0 8px; }
  .contact-company { font-size: 13px; color: var(--accent); }
  .contact-address { font-size: 13px; line-height: 1.35; margin-bottom: 6px; }
  .contact-list { list-style: none; font-size: 13px; line-height: 1.45; }
  .contact-list li { display: flex; align-items: center; gap: 8px; }
  .contact-list svg { width: 12px; height: 12px; flex: none; fill: var(--accent); }
</style>
</head>
<body>
<main class="canvas">

  <section class="card card-front" aria-label="Card front">
    <div>
      <div class="brand"><span class="brand-dot"></span>Veltrano</div>
      <span class="brand-est">EST. 1979</span>
    </div>
  </section>

  <section class="card card-back" aria-label="Card back">
    <div class="back-logo">
      <div class="brand"><span class="brand-dot"></span>Veltrano</div>
      <span class="brand-est">EST. 1979</span>
    </div>
    <span class="divider"></span>
    <div class="contact">
      <p class="contact-name">Tomás Ervedal</p>
      <p class="contact-role">Manager</p>
      <p class="contact-company">Veltrano, LDA</p>
      <p class="contact-address">Rua das Oliveiras, 42<br>1900-114 Lisboa</p>
      <ul class="contact-list">
        <li>
          <svg viewBox="0 0 12 12" aria-hidden="true"><rect x="3" y="0.5" width="6" height="11" rx="1.2"/><rect x="4.2" y="1.8" width="3.6" height="7" fill="#1c1f23"/></svg>
          +351 912004815
        </li>
        <li>
          <svg viewBox="0 0 12 12" aria-hidden="true"><path d="M2.4 0.8l2 2.2-1 1.4c.8 1.7 2 2.9 3.7 3.7l1.4-1 2.2 2-1.2 2C5 10.8 1.2 7 .6 2z"/></svg>
          +351 210007362
        </li>
        <li>
          <svg viewBox="0 0 12 12" aria-hidden="true"><rect x="0.5" y="2" width="11" height="8" rx="1"/><path d="M1 2.6l5 3.8 5-3.8" fill="none" stroke="#1c1f23" stroke-width="1"/></svg>
          geral@veltrano.pt
        </li>
        <li>
          <svg viewBox="0 0 12 12" aria-hidden="true"><circle cx="6" cy="6" r="5.5"/><path d="M.5 6h11M6 .5c-2.4 3-2.4 8 0 11M6 .5c2.4 3 2.4 8 0 11" fill="none" stroke="#1c1f23" stroke-width=".8"/></svg>
          www.veltrano.pt/oficina
        </li>
      </ul>
    </div>
  </section>

</main>
</body>
</html>
```